Relaunch website sonnenundrhein.de

We are looking for creative minds to relaunch the website for our award-winning comedy musical “Wolken und Brise” (www.sonnenundrhein.de). The aim is a cheeky, funny and surprising website that underlines our position as “Germany's funniest musical” and motivates people to buy tickets. The site should convey the positive Cologne attitude to life, be responsive and offer intuitive navigation.

Design specifications: Magenta-purple as the main color with golden accents. Font: Bebas Neue for headlines, Open Sans Condensed for body text.
The heart logo is to be placed at the top left. Various key visuals such as a drawn Cologne skyline or other drawings etc. should be integrated.

In addition to the main page, the subpages: The Musical, Ticket Info, Plan a Visit, Company Events are to be created.

The winner will be selected according to the following criteria: Creativity, user guidance, technical feasibility and compliance with the style guide.

I have uploaded briefing documents in English If you have any questions, please contact lukas.brandt@veltora-buehne.

Further briefings and the style guide have been uploaded in the appendix.

Additionally, graphics can be downloaded under these links (the download of the files takes longer):

http://VELTORA-NAS.fernlager.example/d/s/12hIMn5Y8tBxruv0eqvaTYrfzCXX1ZXE/W2t9gugGTtFgGl2YAyfn0qzz0Jvma2EO-j7YglkhkKww

Link LOGO:
http://VELTORA-NAS.fernlager.example/d/s/12hzRrDEelalG3eIQ1zqq10t7HylrWfW/Y4BTw-kx2bB6SC1pgNFkVCuC0_7yzXY5-XLpAKylVKww

http://VELTORA-NAS.fernlager.example/d/s/12lNTwd0im1cftcjvYC45mULZ0Fh0YTU/rlBvu8wD4UG6w7gLlYP8xqw2kmzaoiy1-H7sAETBWKww

Target Market(s)

Germany-wide + region 40 kilometers around Cologne

Industry/Entity Type

Entertaunment Produktion

Coding

Coded - Design and coding required

Number of Pages Required

4 page

Font styles to use
Other font styles liked:
• Bebas Neue , Open Sans Condensed

Colors
E54698
E96AAD
F1A4CE
F9D9EA
FCEFF6
A7469A
B969AE
D3A5CF
EDDBEB
F8F0F9

Requirements
Must have
• Color scheme • Main color: magenta-violet • Accent color: gold/gold tones • Complementary colors: shades of the main color and neutral tones for body text Typography • Headlines: Bebas Neue (sans-serif, no italics or small capitals) • Copy texts: Open Sans Condensed (all styles allowed, no italics) • Clear hierarchy for optimal readability and recognition Logo • The heart logo must always appear on a heart-shaped background • Variants with the addition "The Cologne Musical" are possible • Prominent placement in all areas of the website Key visuals • Combination of striking illustrations with local Cologne symbols • Cologne skyline with cathedral and TV tower • Golden accents and rainbow elements • Kölsch glass as a local reference • Stylized graphic elements in gold (stars, glitter effects, frames) Website structure and content Header area • Dynamic news ticker with current offers and performance dates • Logo (left) and main navigation (right) • Prominently placed "Get Tickets" button in gold • Main menu items: Musical, Ticket Info, Plan Visit, Groups, Corporate Events, FAQ Hero Section • Emotionally effective video background or changing key visuals • Concise headline: "WOLKEN UND BRISE - The award-winning Cologne musical" • Subheadline with a special humorous component • Eye-catching CTA button "GET TICKETS" with price information Celebrity Endorsement Section • Creative slider concept with testimonials from well-known personalities • Integration of quotes from Marlene Oswitz, Reinhard Plomberg, Dieter Hanslik • Authentic representation of the celebrities in connection with the musical Awards & Headlines • Visual highlighting of the awards • Infographic on visitor numbers (144. 000+) and recommendation rate • Integration of the four German musical and theater awards as badges/icons Show description • Humorous presentation of the plot surrounding Pastor Gunnar • Creative visualization of the show highlights • List of special features (live orchestra, choreography, etc. ) • Integration of Cologne local flavor Press reviews slider • Dynamic concept for presenting press reviews • Integration of quotes from Blatt zum Montag, Kurier, Rheinische Morgenpost • Visual linking with the respective media logos Highlight scenes • Interactive photo gallery with short, witty descriptions • Potential integration of short video snippets • "Appetizers" without giving too much away about the musical USP section • Four concise icons with accompanying text • Highlighting the unique selling points: live orchestra, unique venue, sustainability, Cologne culture • Creative implementation of the icons in the style of the musical Voucher banner • Eye-catching design for the voucher area • Emotional appeal: "Give the gift of unforgettable moments" • Direct CTA for voucher ordering Visitor comments • Authentic testimonials with real visitor photos • Representation of various target group representatives • Integration of "people next door" perspectives Experience Cologne banner • Linking the musical with Cologne sights • Communicating the "Cologne experience" • Strong CTA for ticket booking Corporate events section • Presentation of business offers • Showcasing the possible combinations of business and pleasure • Presentation of VIP packages and special arrangements Quick links • Six attractively designed image tiles • Intuitive navigation to important subsections • Subject areas: Arrival & parking, ticket categories, performance times, corporate events, group offers, FAQ Footer area • Newsletter registration with emotional incentive • Clear contact information • Social media integration (Frendly, Pixaroo, Vidplex, Flipzy) • Area for legal information Functional requirements Responsive design • Optimal display on all devices (desktop, tablet, smartphone) • Special attention to mobile-first approach Performance • Fast loading times despite multimedia content • Optimization of all images and videos SEO optimization • SEO-friendly URL structure • Meta information for all pages • Semantic HTML structure • Keyword optimization for "Musical Cologne", "Comedy Musical", etc. • Special requirements for the wireframe Tonality and creativity The wireframe should already convey the cheeky, witty tone of the musical. Look for surprising elements that make you smile and capture the Cologne way of life. Integrate Cologne humor into UI elements, navigation terms, or micro-interactions. User path to ticket purchase Show how you can guide the user to ticket purchase through clever UX design. Pay particular attention to: • Strategic placement of calls to action • Reducing click paths to ticket purchases • Emotional triggers at decision points Surprising interaction elements Design unusual interaction elements that fit the character of the musical: • Cologne Cathedral that "sings" on hover • Interactive Cologne city scenes • Humorous loading animations • Easter eggs that appeal to Cologne insider knowledge Multi-device concept Show how your ideas work on different devices. Particularly important: • How navigation works on mobile devices • How complex elements like the seating plan are displayed on small screens • Which content is prioritized on mobile
Nice to have
• See briefing

```html
<!DOCTYPE html>
<html lang="en">
<head>
<meta charset="utf-8">
<title>Wolken und Brise – Cologne Musical</title>
<link rel="stylesheet" href="https://fonts.googleapis.com/css2?family=Bebas+Neue&family=DM+Sans:wght@400;500;700&family=Open+Sans:wdth,wght@75,300;75,400&family=Poppins:wght@500;600;700&display=swap">
<style>
:root{
  --magenta:#E0149F;
  --magenta-card:#E53AAE;
  --blush:#FCE9F5;
  --lilac:#EBC8EF;
  --gold:#F9B200;
  --gold-dark:#A7780A;
  --violet-btn:#B64FDC;
  --ink:#1E1E22;
  --navy:#0B0493;
  --navy-deep:#03015E;
  --lime:#86D84A;
  --white:#FFFFFF;
}
*{margin:0;padding:0;box-sizing:border-box}
html,body{width:1200px;height:4697px;overflow:hidden;background:var(--white)}
body{position:relative;font-family:"DM Sans",sans-serif;color:var(--ink)}
.abs{position:absolute}

/* Testimonials */
.testimonials{position:absolute;left:33px;top:0;width:1134px;height:548px;background:var(--magenta)}
.review{position:absolute;width:306px;background:var(--magenta-card);border-radius:12px;padding:0 33px;color:var(--white)}
.review .stars{color:var(--gold);font-size:20px;letter-spacing:4px;margin-top:22px}
.review h3{font-family:"Poppins",sans-serif;font-weight:600;font-size:16px;line-height:21px;margin-top:8px;height:44px}
.review p{font-size:9.5px;line-height:14px;margin-top:12px;opacity:.9}
.review .name{color:var(--lime);font-size:13px;margin-top:30px}
.review.cut p{margin-top:0}
.review.cut .name{margin-top:16px}

/* Corporate */
.corporate{position:absolute;left:33px;top:589px;width:1134px;height:538px;background:var(--blush)}
.corporate h2{position:absolute;left:84px;top:84px;font-family:"Poppins",sans-serif;font-weight:700;font-size:40px;line-height:49px;color:var(--ink)}
.corporate h2 em{font-style:normal;color:var(--magenta)}
.corporate .intro{position:absolute;left:84px;top:210px;font-size:15px;color:#444}
.perks{position:absolute;left:84px;top:260px;list-style:none}
.perks li{display:flex;align-items:center;gap:10px;height:40px;font-weight:700;font-size:15px}
.perks .tick{width:26px;height:26px;border-radius:50%;background:var(--magenta);display:flex;align-items:center;justify-content:center}
.corporate .foot{position:absolute;left:84px;top:433px;font-size:15px;color:#444}
.corporate .back{position:absolute;left:633px;top:104px;width:417px;height:303px;background:var(--lilac);border-radius:12px}
.corporate .photo{position:absolute;left:604px;top:131px;width:417px;height:301px;border-radius:12px;background:linear-gradient(135deg,#8a8f98,#3c4250 55%,#c9b6a4);box-shadow:0 6px 18px rgba(0,0,0,.2)}

/* Discover Cologne */
.discover{position:absolute;left:33px;top:1477px;width:1134px;height:2217px;background:var(--magenta)}
.city-banner{position:absolute;left:80px;top:1169px;width:1042px;height:615px;border-radius:14px;background:linear-gradient(180deg,#5968D8 0%,#7353C8 45%,#6A3A96 100%);box-shadow:0 8px 22px rgba(0,0,0,.25);overflow:hidden}
.city-banner span{position:absolute;left:0;right:0;top:232px;text-align:center;font-family:"Bebas Neue",sans-serif;font-size:152px;line-height:1;color:var(--gold)}
.discover h2{position:absolute;left:0;right:0;top:411px;text-align:center;font-family:"Bebas Neue",sans-serif;font-size:86px;line-height:1;color:var(--gold);font-weight:400}
.discover p{position:absolute;left:232px;width:670px;top:505px;text-align:center;font-family:"Open Sans",sans-serif;font-stretch:75%;font-weight:300;font-size:27px;line-height:37px;color:var(--white)}
.cta{position:absolute;left:434px;top:730px;width:266px;height:73px;background:var(--violet-btn);border-radius:4px;display:flex;align-items:center;justify-content:center;gap:18px;font-family:"Bebas Neue",sans-serif;font-size:26px;color:var(--gold)}
.tile{position:absolute;width:292px;height:310px;background:var(--gold);border-radius:4px;overflow:hidden;box-shadow:0 3px 6px rgba(0,0,0,.15)}
.tile svg{position:absolute;left:86px;top:84px}
.tile .label{position:absolute;left:0;bottom:0;width:100%;height:58px;background:var(--gold-dark);color:var(--white);font-family:"Bebas Neue",sans-serif;font-size:30px;display:flex;align-items:center;justify-content:center}
.skyline{position:absolute;left:0;top:1733px;width:1134px;height:484px;background:linear-gradient(180deg,rgba(224,20,159,0) 0%,#8E22B8 45%,#2A10B0 80%,var(--navy) 100%)}

/* Footer */
.site-footer{position:absolute;left:33px;top:3694px;width:1134px;height:970px;background:var(--navy);color:var(--white)}
.newsletter h3{position:absolute;left:0;right:0;top:127px;text-align:center;font-size:15px;font-weight:700}
.newsletter p{position:absolute;left:430px;width:274px;top:156px;text-align:center;font-size:9px;line-height:11px}
.newsletter form{position:absolute;left:383px;top:197px;width:368px;height:46px;background:var(--white);border-radius:4px;border:3px solid var(--white)}
.newsletter input{border:0;outline:0;font-family:"DM Sans",sans-serif;font-size:11px;padding:0 14px;height:40px;width:240px;color:#666}
.newsletter button{position:absolute;right:2px;top:2px;width:118px;height:36px;background:var(--navy-deep);color:var(--white);border:0;border-radius:3px;font-family:"DM Sans",sans-serif;font-size:11px;font-weight:700}
.contact-item{position:absolute;left:128px;display:flex;gap:28px}
.contact-item b{display:block;font-size:15px;font-weight:500}
.contact-item small{display:block;font-size:9px;margin-top:5px}
.links{position:absolute;top:337px;list-style:none}
.links h4{font-size:15px;font-weight:500;margin-bottom:25px}
.links li{font-size:10px;height:35px}
.socials{position:absolute;left:126px;top:630px;display:flex;gap:14px}
.socials span{width:19px;height:19px;border-radius:4px;border:2px solid var(--white);display:block}
.rule{position:absolute;left:126px;top:731px;width:883px;height:1px;background:#4a46b4}
.copyright{position:absolute;left:0;right:0;top:823px;text-align:center;font-size:13px;font-weight:700}
</style>
</head>
<body>

<section class="testimonials" aria-label="Visitor comments">
  <article class="review cut" style="left:91px;top:-10px;height:105px">
    <p>progress. They did an excellent job and I would highly recommend them to anyone looking for a quality solar panel installation.</p>
    <div class="name">Sarah Johnson</div>
  </article>
  <article class="review cut" style="left:414px;top:-10px;height:105px">
    <p>worry about a thing. I highly recommend this company to anyone looking for a quality solar panel installation.</p>
    <div class="name">Richard Wilson</div>
  </article>
  <article class="review cut" style="left:737px;top:-10px;height:105px">
    <p>was completely satisfied with the final result. I'm so happy with my new solar panels and I'm saving a lot on my energy bills.</p>
    <div class="name">David Brown</div>
  </article>

  <article class="review" style="left:91px;top:122px;height:252px">
    <div class="stars">★★★★★</div>
    <h3>Top-notch Workmanship from Solvani!</h3>
    <p>I was extremely impressed with the quality of the solar panel installation. The workmanship was top-notch and the panels look great on my roof. I would highly recommend this company to anyone looking for a high-quality solar panel installation.</p>
    <div class="name">Jane Doe</div>
  </article>
  <article class="review" style="left:414px;top:122px;height:252px">
    <div class="stars">★★★★★</div>
    <h3>Affordable and Reliable Services!</h3>
    <p>I was looking for a solar panel company that was affordable and reliable, and I found both with this company. The installation was completed on time and within budget, and the panels are working great. I would definitely use this company again.</p>
    <div class="name">Michael Smith</div>
  </article>
  <article class="review" style="left:737px;top:122px;height:252px">
    <div class="stars">★★★★★</div>
    <h3>Eco-friendly and Convenient Product!</h3>
    <p>I wanted to switch to solar panels because I wanted to be more eco-friendly and save money on my energy bills. This company made the process so convenient, and now I have clean energy powering my home. I couldn't be happier.</p>
    <div class="name">Emily Davis</div>
  </article>
</section>

<section class="corporate" aria-label="Corporate events">
  <h2>The perfect setting for<br>your <em>corporate event.</em></h2>
  <p class="intro">Combine business with pleasure. Use our historic venue for:</p>
  <ul class="perks">
    <li><span class="tick"><svg width="14" height="14" viewBox="0 0 14 14"><path d="M2 7.5l3.2 3L12 3.5" fill="none" stroke="#fff" stroke-width="2" stroke-linecap="round" stroke-linejoin="round"/></svg></span>Meetings &amp; workshops</li>
    <li><span class="tick"><svg width="14" height="14" viewBox="0 0 14 14"><path d="M2 7.5l3.2 3L12 3.5" fill="none" stroke="#fff" stroke-width="2" stroke-linecap="round" stroke-linejoin="round"/></svg></span>Team-building events</li>
    <li><span class="tick"><svg width="14" height="14" viewBox="0 0 14 14"><path d="M2 7.5l3.2 3L12 3.5" fill="none" stroke="#fff" stroke-width="2" stroke-linecap="round" stroke-linejoin="round"/></svg></span>Client receptions</li>
    <li><span class="tick"><svg width="14" height="14" viewBox="0 0 14 14"><path d="M2 7.5l3.2 3L12 3.5" fill="none" stroke="#fff" stroke-width="2" stroke-linecap="round" stroke-linejoin="round"/></svg></span>Christmas parties</li>
  </ul>
  <p class="foot">Including an exclusive VIP musical experience.</p>
  <div class="back"></div>
  <div class="photo" role="img" aria-label="Photo of a business meeting with a presenter at a flipchart"></div>
</section>

<section class="discover" aria-label="Discover Cologne">
  <h2>Discover Cologne at its heavenly best!</h2>
  <p>Embark on a whirlwind journey through shisha bars and breweries, meet Cologne originals, and let yourself be enchanted by the magic of the cathedral city. Wolken und Brise is more than just a musical—it's a love letter to Cologne and its people. Secure your tickets now for an unforgettable experience!</p>
  <a class="cta">Tickets kaufen
    <svg width="38" height="12" viewBox="0 0 38 12"><path d="M0 6h35M30 1l5 5-5 5" fill="none" stroke="#F9B200" stroke-width="1.6"/></svg>
  </a>

  <div class="tile" style="left:87px;top:889px">
    <svg width="120" height="120" viewBox="0 0 120 120" fill="none" stroke="#111" stroke-width="9" stroke-linecap="round" stroke-linejoin="round"><path d="M60 110V70c0-18 20-30 30-40M70 22h22v22"/><path d="M22 28h22v18c0 10-6 16-14 20" fill="#111"/></svg>
    <div class="label">Directions &amp; Parking</div>
  </div>
  <div class="tile" style="left:421px;top:889px">
    <svg width="120" height="120" viewBox="0 0 120 120" fill="none" stroke="#111" stroke-width="8" stroke-linejoin="round"><path d="M45 25l12 8 14-20 38 25-42 68-38-25 14-22-12-8z"/><path d="M8 40l6 22 14-4"/></svg>
    <div class="label">Ticket Categories</div>
  </div>
  <div class="tile" style="left:755px;top:889px">
    <svg width="120" height="120" viewBox="0 0 120 120" fill="none" stroke="#111" stroke-width="8" stroke-linecap="round"><path d="M20 20c22-10 45-8 58 4-4 10-10 16-18 18"/><path d="M20 20c-6 24 0 48 20 55"/><path d="M45 40c25-6 50 4 62 22-4 30-22 50-40 48-16-6-26-34-22-70z"/><path d="M62 66c4-4 8-4 11 0M84 68c4-4 8-4 11 1M70 90c8 5 16 4 20-2"/></svg>
    <div class="label">Show Times</div>
  </div>
  <div class="tile" style="left:87px;top:1241px">
    <svg width="120" height="120" viewBox="0 0 120 120" fill="none" stroke="#111" stroke-width="8" stroke-linejoin="round" stroke-linecap="round"><rect x="12" y="12" width="96" height="96" rx="4"/><path d="M28 90l20-24 14 12 20-26 10 10M30 36h18l12-8"/></svg>
    <div class="label">Corporate Events</div>
  </div>
  <div class="tile" style="left:421px;top:1241px">
    <svg width="120" height="120" viewBox="0 0 120 120" fill="none" stroke="#111" stroke-width="8" stroke-linecap="round"><circle cx="26" cy="26" r="16"/><circle cx="26" cy="94" r="16"/><path d="M38 36l70-30M38 84l30-20M80 86h10M100 86h10"/></svg>
    <div class="label">Group Offers</div>
  </div>
  <div class="tile" style="left:755px;top:1241px">
    <svg width="120" height="120" viewBox="0 0 120 120" fill="none" stroke="#111" stroke-width="8" stroke-linejoin="round" stroke-linecap="round"><path d="M10 12h100v74H62l-18 22V86H10z"/><path d="M48 38c0-10 24-12 24 2 0 10-12 10-12 20"/><circle cx="60" cy="72" r="2" fill="#111"/></svg>
    <div class="label">FAQ</div>
  </div>

  <div class="skyline" role="img" aria-label="Illustrated Cologne skyline with the cathedral and TV tower"></div>
</section>

<div class="city-banner" role="img" aria-label="Photo of the Cologne riverside with the TV tower and modern buildings">
  <span>Köln entdecken</span>
</div>

<footer class="site-footer">
  <div class="newsletter">
    <h3>Subscribe to our Newsletter</h3>
    <p>Stay up-to-date! Sign up for our newsletter to never miss offers or news.</p>
    <form><input type="email" placeholder="Your email address here"><button type="button">Subscribe</button></form>
  </div>

  <div class="contact-item" style="top:337px">
    <svg width="26" height="26" viewBox="0 0 24 24" fill="none" stroke="#fff" stroke-width="1.4"><path d="M5 3h4l2 5-2.5 1.5a11 11 0 005 5L15 12l5 2v4a2 2 0 01-2 2A16 16 0 013 5a2 2 0 012-2z"/></svg>
    <div><b>Contact</b><small>(123) 555-0188</small></div>
  </div>
  <div class="contact-item" style="top:411px">
    <svg width="26" height="26" viewBox="0 0 24 24" fill="none" stroke="#fff" stroke-width="1.4"><rect x="3" y="5" width="18" height="14" rx="2"/><path d="M3 7l9 6 9-6"/></svg>
    <div><b>E-mail</b><small>lukas.brandt@veltora-buehne</small></div>
  </div>
  <div class="contact-item" style="top:487px">
    <svg width="26" height="26" viewBox="0 0 24 24" fill="none" stroke="#fff" stroke-width="1.4"><circle cx="12" cy="12" r="10"/><circle cx="12" cy="11" r="3"/></svg>
    <div><b>Address</b><small>Houston, Texas</small></div>
  </div>
  <div class="contact-item" style="top:561px">
    <svg width="30" height="30" viewBox="0 0 24 24" fill="none" stroke="#fff" stroke-width="1.6"><circle cx="12" cy="12" r="10"/><path d="M12 6v6l4 3"/></svg>
    <div><b>Opening Hours</b><small>1800 - 2300</small></div>
  </div>

  <ul class="links" style="left:438px">
    <h4>Quick Links</h4>
    <li>Home</li><li>Our Services</li><li>About Us</li><li>Contact</li>
  </ul>
  <ul class="links" style="left:571px">
    <h4>Legal</h4>
    <li>Imprint</li><li>Terms &amp; Conditions</li><li>Privacy Policy</li><li>Cookies</li>
  </ul>

  <div class="socials">
    <span aria-label="Pixaroo" style="background:#D84B9A"></span>
    <span aria-label="Frendly" style="background:#2B7BE8"></span>
    <span aria-label="Flipzy" style="background:#111"></span>
    <span aria-label="Vidplex" style="background:#E22222"></span>
  </div>
  <div class="rule"></div>
  <p class="copyright">Copyright © 2025 Wolken und Brise - All Rights Reserved</p>
</footer>

</body>
</html>
```